Cosmetic Dentist Practice needs stationery package/logo

I need a letterhead, envelope and business card for a cosmetic and Dental Inplant practice in an upscale part of Houston. The business card will be a size 3.5 x 2 and the letterhead will be 8.5" x 11" with a standard #10 envelope.
I have uploaded a file with an idea that the dentist had for his cards. Please note that this is not the size that the card should be. It does provide the information required.
Updates
Thank you all for your submissions. They were each unique and special in their own way. My client has made a selection that he feels best meets his needs. I appreciate each of you taking the time to offer designs. Good luck to each of you...I hope to see you back in MarblePost on future projects.
Industry/Entity Type
Business
Look and feel
Each slider illustrates characteristics of the customer's brand and the style your logo design should communicate.

```html
<!DOCTYPE html>
<html lang="en">
<head>
<meta charset="utf-8">
<title>Highridge Stationery – Envelopes</title>
<link rel="stylesheet" href="https://fonts.googleapis.com/css2?family=Open+Sans:wght@300;400&display=swap">
<style>
  :root {
    --stage: #a7a7a7;
    --paper: #ffffff;
    --brand-blue: #00aeef;
    --soft-grey: #d1d3d4;
    --pale-grey: #f2f2f2;
    --mark-grey: #b9bbbe;
    --text-grey: #9a9a9a;
    --ring-blue: #d6edf8;
  }
  * { margin: 0; padding: 0; box-sizing: border-box; }
  html, body { width: 1200px; height: 1000px; overflow: hidden; }
  body {
    background: var(--stage);
    font-family: "Open Sans", Arial, sans-serif;
    position: relative;
  }
  .envelope {
    position: absolute;
    left: 240px;
    width: 720px;
    height: 311px;
    background: var(--paper);
    overflow: hidden;
    box-shadow: 0 4px 14px rgba(0,0,0,0.28);
  }
  .envelope--classic { top: 4px; }
  .envelope--sweep { top: 345px; }
  .envelope--band { top: 685px; }
  .envelope__art { position: absolute; inset: 0; }

  .brand { position: absolute; display: flex; align-items: center; }
  .brand__dot {
    width: 52px; height: 52px; border-radius: 50%;
    background: var(--mark-grey);
    border: 2px solid var(--paper);
    box-shadow: 0 0 0 1.5px var(--brand-blue);
    margin-right: 9px;
    flex: none;
  }
  .brand__name {
    font-weight: 300; font-size: 26px; line-height: 1;
    color: var(--brand-blue); letter-spacing: 0;
    white-space: nowrap;
  }
  .brand__tagline {
    font-size: 7px; color: #6d6e71; margin-top: 3px; margin-left: 2px;
    white-space: nowrap;
  }
  .envelope--classic .brand { left: 31px; top: 27px; }
  .envelope--sweep .brand { left: 27px; top: 28px; }
  .envelope--band .brand { left: 27px; top: 28px; }

  .return-address {
    position: absolute;
    font-weight: 300; font-size: 12.5px; line-height: 15px;
    color: var(--text-grey);
    white-space: nowrap;
  }
  .envelope--classic .divider {
    position: absolute; left: 246px; top: 40px;
    width: 1px; height: 27px; background: #cfcfcf;
  }
  .envelope--classic .return-address { left: 264px; top: 37px; }
  .envelope--sweep .return-address { left: 27px; top: 95px; }

  .footer-band {
    position: absolute; left: 0; top: 219px; width: 100%; height: 38px;
    background: var(--brand-blue);
    color: var(--paper); font-size: 12px; font-weight: 300;
    padding-left: 27px; line-height: 38px;
    white-space: nowrap;
  }
  .footer-base {
    position: absolute; left: 0; top: 257px; width: 100%; height: 54px;
    background: var(--soft-grey);
  }
</style>
</head>
<body>

  <section class="envelope envelope--classic">
    <svg class="envelope__art" viewBox="0 0 720 311" aria-hidden="true">
      <circle cx="620" cy="199" r="152" fill="var(--pale-grey)" stroke="var(--ring-blue)" stroke-width="4"/>
    </svg>
    <div class="brand">
      <span class="brand__dot"></span>
      <div>
        <div class="brand__name">HIGHRIDGE</div>
        <div class="brand__tagline">Cosmetic and Implant Dentistry</div>
      </div>
    </div>
    <span class="divider"></span>
    <p class="return-address">72 Cedar Bend Road Suite 310 N.<br>Fairview, TX. 77099</p>
  </section>

  <section class="envelope envelope--sweep">
    <svg class="envelope__art" viewBox="0 0 720 311" aria-hidden="true">
      <path d="M570 0 C 572 150 480 270 345 311 L720 311 L720 0 Z" fill="var(--soft-grey)"/>
      <path d="M570 0 C 572 150 480 270 345 311" fill="none" stroke="var(--brand-blue)" stroke-width="5"/>
      <circle cx="617" cy="212" r="83" fill="none" stroke="#e2e3e4" stroke-width="3"/>
    </svg>
    <div class="brand">
      <span class="brand__dot"></span>
      <div>
        <div class="brand__name">HIGHRIDGE</div>
        <div class="brand__tagline">Cosmetic and Implant Dentistry</div>
      </div>
    </div>
    <p class="return-address">72 Cedar Bend Road Suite 310 N.<br>Fairview, TX. 77099</p>
  </section>

  <section class="envelope envelope--band">
    <div class="brand">
      <span class="brand__dot"></span>
      <div>
        <div class="brand__name">HIGHRIDGE</div>
        <div class="brand__tagline">Cosmetic and Implant Dentistry</div>
      </div>
    </div>
    <div class="footer-band">72 Cedar Bend Road Suite 310 N. | Fairview, TX. 77099</div>
    <div class="footer-base"></div>
  </section>

</body>
</html>
```